Northvale Seal Works Spray Foam Appications website

We need a custom website for our company, www.northvalesealworks.com. We need something we can modify by adding/changing content, photos, updated projects, etc. We are a commercial contractor specializing in Spray Foam applications. We want the website to be very creative and easy to navigate. The main points of the website are to showcase our projects, and describe our scope of services. We provide spray foam applications to the residential and commercial market. We offer Spray Foam roofing applications, as well as Spray Foam interior insulation applications. We also provide Roof Restoration Coating Systems to refurbish old and failing metal roofs. We would be ok with a one page web design if we can get the scope of our services to flow in a single page. The designer can decide if single or multiple pages works best for our business. One of the suppliers we work with is www.brenvexa.com.

Target Market(s)

Residential Home Builders, General Contractors, Commercial Construction Companies, Property Management Groups.

Industry/Entity Type

Insulation

Number of Pages Required

5+ page

Font styles to use
Serif
Sans Serif

Colors

Designer to choose colors to be used in the design.

Requirements
Must have
• We already have a Wix page, so website must be a Wix theme design. Nice easy to navigate format. Color matched to our current logo theme. We already have brochures and would like for it to match what's already in the hands of some of our customers. Need to be able to manage content to update photos, projects, scope of service, etc., via Wix. Current hold/splash page is hosted at www.northvalesealworks.com. We would also like to have this video posted on the home page: https://www.clipvaultia.com/watch?v=KqT7wPz3LmA&feature=clipvlt.be
Nice to have
• I have attached some splash videos, being able to incorporate these somehow without being overpowering would be nice.

```html
<!DOCTYPE html>
<html lang="en">
<head>
<meta charset="utf-8">
<title>Northvale Seal Works</title>
<link href="https://fonts.googleapis.com/css2?family=Roboto:wght@300;400;500;700&display=swap" rel="stylesheet">
<style>
:root{
  --gold:#f2b01e;
  --black:#000;
  --nav:#1d1d1d;
  --panel:#1e1e1e;
  --news:#232323;
  --white:#fff;
  --muted:#a8a8a8;
  --line:#3a3a3a;
}
*{box-sizing:border-box;margin:0;padding:0}
html,body{width:1200px;height:3854px;overflow:hidden;background:var(--black);font-family:'Roboto',Arial,sans-serif;color:var(--white)}
.page{position:relative;width:1200px;height:3854px}
.abs{position:absolute}
.label{font-size:10px;letter-spacing:2.5px;color:var(--gold);text-transform:uppercase;font-weight:500}
.heading{font-size:27px;font-weight:500;color:var(--white)}
.center{left:0;width:1200px;text-align:center}
.brand{display:flex;align-items:center;gap:9px;white-space:nowrap}
.brand-dot{width:40px;height:40px;border:3px solid var(--gold);border-radius:50%;flex:none}
.brand-name{font-size:13px;font-weight:700;color:var(--gold);letter-spacing:.5px;text-transform:uppercase}
.footer-brand .brand-name{font-size:10px;letter-spacing:0}

/* nav */
.site-nav{left:0;top:0;width:1200px;height:67px;background:var(--nav)}
.site-nav .brand{position:absolute;left:235px;top:13px}
.nav-links{position:absolute;right:234px;top:27px;display:flex;gap:26px;list-style:none;font-size:10px;letter-spacing:1px;font-weight:500}

/* hero */
.hero-photo{left:0;top:67px;width:1200px;height:427px;background:linear-gradient(180deg,#5d5f61 0%,#6d6e6c 45%,#8e8f8d 70%,#a7a8a6 100%)}
.hero-title{top:150px;font-size:39px;font-weight:500;line-height:39px}
.hero-sub{top:267px;font-size:21px;font-weight:300;letter-spacing:.5px}
.video{left:359px;top:361px;width:482px;height:264px;background:linear-gradient(135deg,#6b5a44,#a08462 45%,#7a6350)}
.play{left:564px;top:477px;width:72px;height:34px;border-radius:17px;background:var(--white)}

/* services */
.svc-card{top:829px;width:230px;height:239px;border:1px solid var(--line);padding:42px 36px 0}
.svc-card.active{background:var(--gold);border-color:var(--gold)}
.svc-card h3{font-size:13px;font-weight:500;color:var(--gold);margin-bottom:23px}
.svc-card.active h3,.svc-card.active p{color:var(--white)}
.svc-card p{font-size:10px;line-height:19px;color:var(--muted);font-weight:300}
.svc-card .rule{width:26px;height:2px;background:var(--gold);margin:32px 0 19px}
.svc-card.active .rule{background:var(--black)}
.svc-card .more{font-size:8px;font-weight:700;letter-spacing:1px}

/* about */
.about-panel{left:0;top:1165px;width:797px;height:527px;background:var(--panel)}
.about-photo{left:609px;top:1240px;width:507px;height:377px;background:linear-gradient(180deg,#8b9096 0%,#a9adb1 35%,#c9cbcc 60%,#e2e3e3 100%)}
.about-title{left:235px;font-size:25px;font-weight:500;line-height:30px}
.about-text{left:235px;top:1430px;width:300px;font-size:10.5px;line-height:19px;color:var(--muted);font-weight:300}
.btn-gold{left:235px;top:1557px;width:126px;height:39px;background:var(--gold);font-size:8px;font-weight:700;letter-spacing:1px;display:flex;align-items:center;justify-content:center}

/* cta */
.cta{left:0;top:1692px;width:1200px;height:182px;background:var(--gold)}
.cta-title{left:234px;top:40px;font-size:24px;font-weight:500;line-height:28px}
.cta-text{left:234px;top:106px;width:420px;font-size:10px;line-height:19px;font-weight:300}
.btn-outline{left:827px;top:70px;width:138px;height:42px;border:1.5px solid var(--white);font-size:8px;font-weight:500;letter-spacing:1px;display:flex;align-items:center;justify-content:center}

/* projects */
.shot{background:linear-gradient(180deg,#6e7276,#a3a6a8 50%,#d2d3d2)}
.shot.roof{background:linear-gradient(180deg,#a0a4a9 0%,#b9bcbe 45%,#d8d9d8 100%)}
.shot.interior{background:linear-gradient(180deg,#b7b3a6,#d5d0c3 60%,#7a7772)}
.shot.building{background:linear-gradient(180deg,#d9d6c9,#e6e1cc 50%,#d0cdc4)}
.overlay{background:rgba(242,176,30,.86);display:flex;flex-direction:column;align-items:center;justify-content:center;text-align:center}
.overlay .label{color:var(--white);font-size:8px;margin-bottom:10px}
.overlay strong{font-size:13px;font-weight:500}
.btn-line{left:537px;top:2741px;width:126px;height:39px;border:1.5px solid var(--white);font-size:8px;font-weight:700;letter-spacing:1px;display:flex;align-items:center;justify-content:center}

/* blog */
.post{top:2967px;width:231px}
.post-img{height:151px;background:linear-gradient(180deg,#56749a 0%,#8aa0b6 30%,#cbb98e 55%,#e0cf9f 100%)}
.post time{display:block;margin-top:19px;font-size:8px;color:var(--muted)}
.post h4{margin-top:8px;font-size:13.5px;font-weight:400;line-height:23px}
.post a{display:block;margin-top:5px;font-size:8.5px;color:var(--gold);text-decoration:none}

/* newsletter */
.map{left:0;top:3308px;width:467px;height:303px;background:linear-gradient(135deg,#8d8d8d,#a3a3a3 50%,#929292)}
.news{left:467px;top:3308px;width:733px;height:303px;background:var(--news)}
.field-label{font-size:8px;letter-spacing:.5px}
.field{width:169px;border-bottom:1px solid #555;font-size:9px;font-style:italic;color:#777;padding:0 0 6px 10px}
.btn-reg{left:859px;top:3495px;width:107px;height:37px;background:var(--gold);font-size:8px;font-weight:500;letter-spacing:1px;display:flex;align-items:center;justify-content:center}

/* footer */
.foot-col h5{font-size:9px;font-weight:500;color:var(--gold);letter-spacing:.5px;margin-bottom:15px}
.foot-col li{list-style:none;font-size:10px;color:var(--muted);line-height:25px;display:flex;align-items:center;gap:12px}
.ico{width:16px;height:16px;border-radius:50%;background:var(--gold);display:inline-flex;align-items:center;justify-content:center}
.bottom-bar{left:0;top:3812px;width:1200px;height:42px;background:var(--gold);font-size:8px;text-align:center;line-height:42px}
</style>
</head>
<body>
<div class="page">

<header class="site-nav abs">
  <div class="brand"><span class="brand-dot"></span><span class="brand-name">Northvale Seal Works</span></div>
  <ul class="nav-links"><li>HOME</li><li>ABOUT US</li><li>SERVICES</li><li>OUR PROJECTS</li><li>BLOG</li><li>CONTACT</li></ul>
</header>

<section>
  <div class="hero-photo abs" role="img" aria-label="Industrial plant with freshly coated white metal roof under an overcast sky, darkened"></div>
  <h1 class="hero-title abs center">Specializing in foam and<br>coatings systems for over 20-years</h1>
  <p class="hero-sub abs center">"SOLUTIONS WITH INTEGRITY"</p>
  <div class="video abs" role="img" aria-label="Video still of a worker spraying foam insulation between wall studs"></div>
  <div class="play abs"><svg width="72" height="34" viewBox="0 0 72 34"><path d="M33 13 L40 17 L33 21 Z" fill="#000"/></svg></div>
</section>

<section>
  <p class="label abs center" style="top:743px">Service</p>
  <h2 class="heading abs center" style="top:758px">What We Propose</h2>
  <article class="svc-card active abs" style="left:235px">
    <h3>Foam Insulation</h3>
    <p>Lorem ipsum dolor sit amet, consectetur adipisicing elit, sed do eiusmod tempor incididunt ut labore et dolorecitation</p>
    <div class="rule"></div><span class="more">READ MORE</span>
  </article>
  <article class="svc-card abs" style="left:485px">
    <h3>Foam Roof</h3>
    <p>Lorem ipsum dolor sit amet, consectetur adipisicing elit, sed do eiusmod tempor incididunt ut labore et dolorecitation</p>
    <div class="rule"></div><span class="more">READ MORE</span>
  </article>
  <article class="svc-card abs" style="left:735px">
    <h3>Roof Restoration/Coating</h3>
    <p>Lorem ipsum dolor sit amet, consectetur adipisicing elit, sed do eiusmod tempor incididunt ut labore et dolorecitation</p>
    <div class="rule"></div><span class="more">READ MORE</span>
  </article>
</section>

<section>
  <div class="about-panel abs"></div>
  <p class="label abs" style="left:235px;top:1264px">Who we are</p>
  <h2 class="about-title abs" style="top:1282px">Lorem ipsum dolor<br>sit amet, consectetur<br>adipisicing elit labore et<br>dolore</h2>
  <p class="about-text abs">Ut enim ad minim veniam, quis nostrud exercitation ullamco laboris nisi ut aliquip ex ea commodo consequat. Duis aute irure dolor in reprehenderit in voluptate velit esse cillum dolore eu fugiat nulla pariatur. Excepteur sint occaecat cupidatat non proident.</p>
  <div class="btn-gold abs">READ MORE</div>
  <div class="about-photo abs" role="img" aria-label="Crew member in safety vest spraying white coating on a long metal roof"></div>
</section>

<section class="cta abs">
  <h2 class="cta-title abs">Duis aute irure dolor in reprehenderit<br>in voluptate velit esse</h2>
  <p class="cta-text abs">Nemo enim ipsam voluptatem quia voluptas sit aspernatur aut odit aut fugit, sed quia consequuntur magni dolores eos qui ratione voluptatem sequi nesciunt.</p>
  <div class="btn-outline abs">CONTACT US</div>
</section>

<section>
  <p class="label abs center" style="top:1969px">Our projects</p>
  <h2 class="heading abs center" style="top:1985px">Lorem ipsum dolor</h2>
  <div class="shot abs" style="left:235px;top:2049px;width:356px;height:418px" role="img" aria-label="Industrial facility beside a white foam-coated metal roof"></div>
  <div class="shot interior abs" style="left:235px;top:2486px;width:356px;height:205px" role="img" aria-label="Warehouse interior with sprayed foam insulation on the walls"></div>
  <div class="shot roof abs" style="left:610px;top:2049px;width:356px;height:205px" role="img" aria-label="Wide flat roof coated white with equipment in the distance"></div>
  <div class="shot building abs" style="left:610px;top:2274px;width:356px;height:417px" role="img" aria-label="Metal building with a newly coated roof"></div>
  <div class="overlay abs" style="left:628px;top:2292px;width:319px;height:381px">
    <span class="label">Dolorem ipsum</span><strong>NUMQUAM MODI TEMPORA</strong>
  </div>
  <div class="btn-line abs">MORE PROJECTS</div>
</section>

<section>
  <p class="label abs center" style="top:2886px">Blog</p>
  <h2 class="heading abs center" style="top:2902px">Latest Post</h2>
  <article class="post abs" style="left:235px"><div class="post-img" role="img" aria-label="Coated roof with a safety cone under a blue sky"></div><time>Jan 15 2020</time><h4>Duis aute irure dolor in reprehenderit in voluptate velit esse</h4><a href="#">Read More</a></article>
  <article class="post abs" style="left:485px"><div class="post-img" role="img" aria-label="Coated roof with a safety cone under a blue sky"></div><time>Jan 15 2020</time><h4>Duis aute irure dolor in reprehenderit in voluptate velit esse</h4><a href="#">Read More</a></article>
  <article class="post abs" style="left:735px"><div class="post-img" role="img" aria-label="Coated roof with a safety cone under a blue sky"></div><time>Jan 15 2020</time><h4>Duis aute irure dolor in reprehenderit in voluptate velit esse</h4><a href="#">Read More</a></article>
</section>

<section>
  <div class="map abs" role="img" aria-label="Grey street map of the service area"></div>
  <div class="news abs"></div>
  <p class="label abs" style="left:509px;top:3373px">Subscribe to our newsletter</p>
  <h2 class="abs" style="left:509px;top:3390px;font-size:24px;font-weight:500;letter-spacing:.5px">to stay in touch</h2>
  <div class="abs" style="left:483px;top:3487px"><p class="field-label">NAME</p><p class="field" style="margin-top:12px">your name</p></div>
  <div class="abs" style="left:672px;top:3487px"><p class="field-label">E-MAIL ADDRESS</p><p class="field" style="margin-top:12px">your e-mail</p></div>
  <div class="btn-reg abs">REGISTER</div>
</section>

<footer>
  <div class="brand footer-brand abs" style="left:235px;top:3656px"><span class="brand-dot"></span><span class="brand-name">Northvale Seal Works</span></div>
  <div class="foot-col abs" style="left:422px;top:3655px"><h5>COMPANY</h5><ul><li>About Us</li><li>Our Team</li><li>Services</li><li>Contact</li></ul></div>
  <div class="foot-col abs" style="left:546px;top:3655px"><h5>RESOURCES</h5><ul><li>Get a spray foam estimate</li><li>Lorem ipsum consectetur</li><li>Adipisicing elit</li><li>Eiusmod ut labore</li></ul></div>
  <div class="foot-col abs" style="left:733px;top:3655px"><h5>GET IN TOUCH</h5><ul>
    <li><span class="ico"><svg width="8" height="10" viewBox="0 0 8 10"><path d="M4 0C1.8 0 0 1.7 0 3.8 0 6.6 4 10 4 10s4-3.4 4-6.2C8 1.7 6.2 0 4 0zm0 5.3A1.5 1.5 0 1 1 4 2.3a1.5 1.5 0 0 1 0 3z" fill="#fff"/></svg></span>157 5th Lorem Ipsum, 1234 NYC</li>
    <li><span class="ico"><svg width="9" height="9" viewBox="0 0 9 9"><path d="M2 0.5 3.4 2.6 2.5 3.6C3 4.8 4.2 6 5.4 6.5L6.4 5.6 8.5 7 7.7 8.5C4 8.3 0.7 5 0.5 1.3Z" fill="#fff"/></svg></span>1 555-014-2087</li>
    <li><span class="ico"><svg width="9" height="7" viewBox="0 0 9 7"><rect x=".5" y=".5" width="8" height="6" fill="none" stroke="#fff"/><path d="M.5.5 4.5 4 8.5.5" fill="none" stroke="#fff"/></svg></span>hello@northvalesealworks.com</li>
  </ul></div>
  <div class="bottom-bar abs">©2020 by Northvale Seal Works, LLC. All rights reserved</div>
</footer>

</div>
</body>
</html>
```